Health and Fitness Club requires membership pack

We need a membership pack, like this style (http://www.sleevepressworks.co.uk/images/A4_pocket_folder_round.jpg) a4 sized.

The front of it should contain our logo, the entire thing should be in the style of our brand/concept. On the inside left side there should be space for copy which we will provide once the design has been selected (approximately 500 words).

At the bottom of the left page inside, should be the following:
telephone icon | bbm icon
instagram logo | twitter logo | kik logo | email logo

with the relevant contact details for our company, underneath this should be our website written so that it occupies the entire width of the page.

our website is www. v i g o r b a s e . ae and our logo is attached

i have included a flyer we recently produced to give you an idea of the creative direction of the brand..

```html
<!DOCTYPE html>
<html lang="en">
<head>
<meta charset="utf-8">
<title>Vigor Base – Membership Pack Folder</title>
<link href="https://fonts.googleapis.com/css2?family=Arimo:wght@400;700&display=swap" rel="stylesheet">
<style>
  :root {
    --backdrop: #ece9e4;
    --paper: #ffffff;
    --grey-light: #f4f4f5;
    --grey-mid: #cfd0d2;
    --brand-red: #ec1c24;
    --brand-black: #050505;
    --ink: #2b2b2b;
    --photo-warm: #e7ddd6;
    --photo-cool: #d9e6ea;
  }
  * { box-sizing: border-box; margin: 0; padding: 0; }
  html, body {
    width: 1200px; height: 1132px; overflow: hidden;
    background: var(--backdrop);
    font-family: "Arimo", Arial, sans-serif;
  }
  .folder { position: relative; width: 1200px; height: 1132px; }

  .inside-left {
    position: absolute; left: 44px; top: 23px; width: 556px; height: 769px;
    background: linear-gradient(90deg, var(--paper) 0%, var(--grey-light) 35%, var(--grey-mid) 100%);
    box-shadow: 0 4px 14px rgba(0,0,0,.28);
  }
  .front-cover {
    position: absolute; left: 600px; top: 23px; width: 555px; height: 769px;
    background: var(--paper);
    box-shadow: 4px 4px 14px rgba(0,0,0,.28);
    overflow: hidden;
  }
  .cover-photo {
    position: absolute; left: 0; top: 0; width: 555px; height: 600px;
    background:
      linear-gradient(180deg, rgba(255,255,255,0) 35%, var(--paper) 95%),
      linear-gradient(90deg, var(--photo-cool) 0%, var(--photo-warm) 45%, var(--photo-cool) 100%);
  }
  .cover-bands { position: absolute; left: 0; top: 0; }

  .pocket-flap {
    position: absolute; left: 103px; top: 792px; width: 497px; height: 274px;
    background: var(--brand-red);
    border-bottom-left-radius: 78px;
    box-shadow: 3px 6px 12px rgba(0,0,0,.35), inset 0 0 0 4px rgba(0,0,0,.08);
  }

  .brand-mark {
    position: absolute; display: flex; align-items: center; gap: 8px;
    font-weight: 700; letter-spacing: 1px; text-transform: uppercase;
    color: var(--brand-black); transform: translateX(-50%); white-space: nowrap;
  }
  .brand-mark .dot {
    width: 22px; height: 22px; border-radius: 50%; background: var(--brand-red);
  }
  .brand-mark--cover { left: 291px; top: 375px; font-size: 32px; }
  .brand-mark--cover .dot { width: 30px; height: 30px; }
  .brand-mark--left { left: 278px; top: 628px; font-size: 22px; }
  .brand-mark--flap { left: 245px; top: 108px; font-size: 26px; color: var(--paper); }
  .brand-mark--flap .dot { background: var(--brand-black); }

  .contact-block {
    position: absolute; left: 0; right: 0; top: 674px;
    text-align: center; color: var(--ink);
  }
  .contact-address { font-size: 16px; }
  .contact-lines {
    margin-top: 8px; display: flex; justify-content: center; gap: 12px; font-size: 13px;
  }
  .contact-item { display: flex; align-items: center; gap: 4px; }
  .contact-item svg { width: 11px; height: 11px; fill: var(--ink); }
  .contact-website {
    margin: 14px 18px 0;
    display: flex; justify-content: space-between;
    font-size: 17px; font-weight: 700; color: var(--brand-black);
  }
</style>
</head>
<body>
<div class="folder">

  <section class="inside-left">
    <div class="brand-mark brand-mark--left"><span class="dot"></span>Vigor Base</div>
    <div class="contact-block">
      <p class="contact-address">#0000, Street Name, Area Name, city Name Country Code.</p>
      <div class="contact-lines">
        <span class="contact-item">
          <svg viewBox="0 0 10 10"><path d="M2 0h2l1 3-1.5 1a6 6 0 0 0 2.5 2.5L7 5l3 1v2a2 2 0 0 1-2 2A8 8 0 0 1 0 2a2 2 0 0 1 2-2z"/></svg>000-XXX-0000
        </span>
        <span class="contact-item">
          <svg viewBox="0 0 10 10"><rect x="2.5" y="0" width="5" height="10" rx="1"/></svg>000-XXX-0000
        </span>
        <span class="contact-item">
          <svg viewBox="0 0 10 10"><rect x="0" y="3" width="10" height="5" rx="1"/><rect x="2" y="0" width="6" height="3"/></svg>000-XXX-0000
        </span>
        <span class="contact-item">
          <svg viewBox="0 0 10 10"><path d="M0 2h10v6H0z M0 2l5 3.5L10 2" fill="none" stroke="#2b2b2b" stroke-width="1.2"/></svg>yourname@mail.com
        </span>
      </div>
      <p class="contact-website" aria-label="www.vigorbase.ae">
        <span>w</span><span>w</span><span>w</span><span>.</span>
        <span>v</span><span>i</span><span>g</span><span>o</span><span>r</span>
        <span>b</span><span>a</span><span>s</span><span>e</span>
        <span>.</span><span>a</span><span>e</span>
      </p>
    </div>
  </section>

  <section class="front-cover">
    <div class="cover-photo" role="img" aria-label="Bright photograph of a group fitness class exercising with light hand weights, fading to white"></div>
    <svg class="cover-bands" width="555" height="769" viewBox="0 0 555 769">
      <line x1="0" y1="769" x2="555" y2="459" stroke="var(--brand-black)" stroke-width="1.5"/>
      <polygon points="10,769 331,590 331,769" fill="var(--brand-red)"/>
      <polygon points="331,590 555,465 555,769 331,769" fill="var(--brand-black)"/>
    </svg>
    <div class="brand-mark brand-mark--cover"><span class="dot"></span>Vigor Base</div>
  </section>

  <section class="pocket-flap">
    <div class="brand-mark brand-mark--flap"><span class="dot"></span>Vigor Base</div>
  </section>

</div>
</body>
</html>
```